Democracy in crisis book

This book tries to sound the ALARM that we will lose our democracy unless we force Unionists to adopt the plan inside this book. I designed a mock cover (attached) but I am concerned it would not look good in the Thumbnail view that most people would see it as they're scrolling down Shopvale or Pagenook. The final title for the book is: Final Hour to Rescue the Free Republic. The current subtitle is: The Single Path to Halt the 2022 Partisan Takeover & Renew Our Homeland -- but it’s a work in progress.The subtitle is still working progress but it's really not that important and can be small.
STYLE CONSIDERATIONS:
(1) The title should be on 5 separate lines: Final; Hour; To Rescue; Free; Republic
(2) The title could be in white fat letters except for maybe one line that says “To Rescue” which could be in the blue color of the Civic Union Party-- or maybe Free Republic could be in blue. We may have to try a few variations of that.
(3) I picked the red in the mock cover to connotate an emergency,
(4) I liked big bold fat font going across the full page so that it looks like a major warning sign, though note I was unable to extend each line flush all the way to the right which I think would have been better.
(5) I liked it better flush to left instead of centered.
(6) I picked the Harwick monument + a crowd for my mock cover, but a picture of a huge crowd protesting with a picture of the United States Congress in the background would be much better. DO NOT USE HARWICK. Obviously I would need it to be an open license or something I can pay a small amount to get. If you can find that picture then the page should probably be colored in red with Congress in white.
I got the idea 4 giant title from the book “seldom a quiet so bright” and Dellowby’s “When Freedom Fades” or “Grey Herons” by Mara Vostell though I hate that font)
I love Osric Thale’s “marked since the outset” cover so if you find a picture of Congress and a protest crowd instead of painting it red you could have just a couple of jagged red stripes going across it like that cover.
I love the 3-D effect of Greta Wolven's cover for The Silverwren where it looks like a page is being ripped. That effect could be done the words Free Republic like it's being torn off the page UPDATE: MANY DESIGNERS TRIED THAT & IT DID NOT WORK AT ALL.
Note that this book will be submitted to many award competitions, so please give me an award-winning cover.
I like how the title of the book The Unchosen by Martin Fellowes has the words starting to fade. I don't like the ladder on it, but maybe 'Free Republic' could fade like that.
Unionists

```html
<!DOCTYPE html>
<html lang="en">
<head>
<meta charset="utf-8">
<title>Final Hour to Rescue the Free Republic – Book Cover</title>
<link rel="stylesheet" href="https://fonts.googleapis.com/css2?family=Figtree:wght@300;800&family=Libre+Baskerville&display=swap">
<style>
  :root {
    --page-bg: #e6e6e6;
    --alarm-red: #b00000;
    --deep-red: #7a0000;
    --night: #120000;
    --party-blue: #4747ff;
    --paper-white: #ffffff;
  }
  * { margin: 0; padding: 0; box-sizing: border-box; }
  html, body {
    width: 1200px;
    height: 964px;
    overflow: hidden;
    background: var(--page-bg);
  }
  .cover {
    position: absolute;
    left: 338px;
    top: 89px;
    width: 524px;
    height: 786px;
    overflow: hidden;
    background: var(--night);
  }
  .cover-art {
    position: absolute;
    inset: 0 0 80px 0;
    background:
      linear-gradient(180deg, var(--alarm-red) 0%, #a20000 30%, var(--deep-red) 55%, #3a0000 78%, var(--night) 100%);
  }
  .title {
    position: absolute;
    left: 30px;
    top: 58px;
    font-family: "Figtree", "Avenir Next", sans-serif;
    text-transform: uppercase;
    line-height: 75px;
    font-size: 88px;
    letter-spacing: -1px;
  }
  .title-line { display: block; white-space: nowrap; }
  .title-line--heavy { font-weight: 800; color: var(--paper-white); text-shadow: 0 2px 4px rgba(0,0,0,.35); }
  .title-line--light { font-weight: 300; color: var(--paper-white); }
  .title-line--blue  { font-weight: 800; color: var(--party-blue); }
  .subtitle {
    position: absolute;
    left: 35px;
    top: 500px;
    width: 470px;
    font-family: "Libre Baskerville", "Baskerville", serif;
    font-size: 22px;
    line-height: 32px;
    color: var(--paper-white);
  }
  .author-band {
    position: absolute;
    left: 0;
    bottom: 0;
    width: 100%;
    height: 80px;
    background: var(--party-blue);
    display: flex;
    align-items: center;
    justify-content: center;
  }
  .author {
    font-family: "Libre Baskerville", "Baskerville", serif;
    font-size: 19px;
    color: var(--paper-white);
  }
</style>
</head>
<body>
  <main class="cover">
    <div class="cover-art" role="img" aria-label="Photograph of the United States Capitol dome above a large protest crowd, tinted red fading to black"></div>
    <h1 class="title">
      <span class="title-line title-line--heavy">Final</span>
      <span class="title-line title-line--heavy">Hour</span>
      <span class="title-line title-line--light">To Rescue</span>
      <span class="title-line title-line--blue">Free</span>
      <span class="title-line title-line--blue">Republic</span>
    </h1>
    <p class="subtitle">This Is Your Warning, Here Is The Plan To Rescue It &amp; These Are The Actions You Must Take Now</p>
    <footer class="author-band">
      <p class="author">by: Corwin Ashby Delane</p>
    </footer>
  </main>
</body>
</html>
```